Cosmetics Brand Logo and Bottle Label Design

We are creating a new cosmetics brand called "Nolan Whitby" and would like you to create an amazing logo and bottle label for this brand's new 100% pure argan oil product.
For the logo, we really like the logo's of Marin Calloway and Vessa. The text should be Sans Serif (without feet).
For the actual bottle label, please find attached labels of one of our competitors design which really like. We really like the simplicity and elegance of the design. The only difference is that our product will be using light turqoise as the brand color. Please feel free to add your own creativity into it as well.
Industry/Entity Type
Cosmetics
Logo Text
Nolan Whitby
Font styles to use

```html
<!DOCTYPE html>
<html lang="en">
<head>
<meta charset="utf-8">
<title>Nolan Whitby – Argan Oil Label</title>
<link rel="stylesheet" href="https://fonts.googleapis.com/css2?family=Source+Sans+3:wght@300;400;600&family=Tenor+Sans&display=swap">
<style>
  :root {
    --paper: #ffffff;
    --label-bg: #7ecabe;
    --label-ink: #23a48d;
    --label-line: #b9e7e1;
    --brand: #25b096;
    --soft-white: #f4fbfa;
    --crop: #1fa88f;
    --footer: #404040;
    --footer-edge: #9a9a9a;
  }
  * { margin: 0; padding: 0; box-sizing: border-box; }
  html, body { width: 1200px; height: 818px; overflow: hidden; background: var(--paper); }
  body { position: relative; font-family: "Source Sans 3", Arial, sans-serif; }

  .crop-marks { position: absolute; inset: 0; }

  .label {
    position: absolute; left: 95px; top: 60px; width: 1010px; height: 396px;
    background: var(--label-bg); border: 1px solid var(--label-line);
  }
  .label__safe {
    position: absolute; left: 11px; top: 10px; width: 988px; height: 376px;
    border: 1px solid var(--label-line);
  }
  .label__fold { position: absolute; top: 0; width: 1px; height: 100%; background: var(--label-line); }
  .label__fold--a { left: 336px; }
  .label__fold--b { left: 672px; }

  .copy { position: absolute; color: var(--label-ink); font-weight: 300; font-size: 10.2px; line-height: 13.7px; }
  .copy p + p { margin-top: 15px; }
  .copy strong { font-weight: 600; }
  .copy--usage { left: 41px; top: 53px; width: 250px; }
  .copy--ingredients { left: 747px; top: 53px; width: 172px; }
  .copy--directions { left: 747px; top: 304px; width: 150px; font-size: 7.4px; line-height: 9.6px; }

  .back-sign { position: absolute; left: 86px; top: 318px; width: 260px; text-align: center; color: var(--label-ink); }
  .back-sign__name { font-family: "Tenor Sans", Arial, sans-serif; font-size: 8.5px; }
  .back-sign__maker { font-size: 7.4px; font-weight: 300; margin-top: 2px; }

  .front-title {
    position: absolute; left: 375px; top: 333px; transform-origin: 0 0; transform: rotate(-90deg);
    color: var(--label-ink); white-space: nowrap;
  }
  .front-title__brand { font-weight: 400; font-size: 41px; line-height: 38px; letter-spacing: 0.5px; }
  .front-title__product { font-weight: 400; font-size: 24.5px; line-height: 28px; letter-spacing: 0.3px; }

  .front-name {
    position: absolute; left: 478px; top: 96px; width: 150px;
    font-family: "Tenor Sans", Arial, sans-serif; font-size: 44px; line-height: 54px;
    color: var(--soft-white);
  }
  .front-type { position: absolute; left: 478px; top: 293px; font-size: 21px; color: var(--label-ink); }
  .front-volume { position: absolute; left: 478px; top: 341px; font-size: 16.5px; color: var(--label-ink); }

  .shelf-life { position: absolute; left: 747px; top: 340px; display: flex; align-items: center; gap: 2px; color: var(--label-ink); font-size: 9.5px; font-weight: 300; }

  .wordmark { position: absolute; font-family: "Tenor Sans", Arial, sans-serif; color: var(--brand); white-space: nowrap; }
  .wordmark--stacked { left: 196px; top: 560px; width: 170px; text-align: center; }
  .wordmark__dot { width: 70px; height: 70px; border-radius: 50%; background: var(--brand); margin: 0 auto 14px; }
  .wordmark__text { font-size: 23px; }
  .wordmark--monogram { left: 545px; top: 574px; font-size: 31px; line-height: 36px; text-align: center; width: 112px; }
  .wordmark--line { left: 808px; top: 588px; font-size: 33px; }

  .footer-band { position: absolute; left: 0; top: 744px; width: 1200px; height: 74px; background: var(--footer); border-top: 4px solid var(--footer-edge); }
</style>
</head>
<body>
  <svg class="crop-marks" width="1200" height="818" viewBox="0 0 1200 818" aria-hidden="true">
    <g stroke="var(--crop)" stroke-width="1.4">
      <line x1="106" y1="10" x2="106" y2="48"/>
      <line x1="1094" y1="10" x2="1094" y2="48"/>
      <line x1="106" y1="469" x2="106" y2="507"/>
      <line x1="1094" y1="469" x2="1094" y2="507"/>
      <line x1="43" y1="70" x2="83" y2="70"/>
      <line x1="1118" y1="70" x2="1158" y2="70"/>
      <line x1="43" y1="446" x2="83" y2="446"/>
      <line x1="1118" y1="446" x2="1158" y2="446"/>
    </g>
  </svg>

  <section class="label">
    <div class="label__safe"></div>
    <div class="label__fold label__fold--a"></div>
    <div class="label__fold label__fold--b"></div>

    <div class="copy copy--usage">
      <p><strong>Suggested Usage:</strong> Lorem ipsum dolor sit amet, consectetur adipiscing elit. Suspendisse eu justo augue. Suspendisse pretium lorem id varius iaculis. Pellentesque vehicula tellus non tincidunt ornare. Curabitur quis turpis diam. Proin vitae euismod ex. Nulla eget luctus massa.</p>
      <p>Argan Oil is a natural plant based product made from the fruit kernal of an argan tree. It is used as a great natural skin moisturiser to hydrate and soften skin. The oil absorbs easily, is non-irritating and non-greasy. Rich in vitamin E it gives the skin a natural boost.</p>
      <p><strong>Warning:</strong> Phasellus maximus quis urna sit amet sodales. Nam felis mi, blandit ut posuere et, rhoncus sed tellus. Nulla nulla est, hendrerit eget volutpat in, pulvinar id quam. Cras tristique dapibus massa, nec suscipit libero ultricies sed. Praesent tincidunt nisi eu augue tristique tempus.</p>
    </div>

    <div class="back-sign">
      <div class="back-sign__name">Nolan Whitby</div>
      <div class="back-sign__maker">Manufactured by xxxx &nbsp;www.nolanwhitby.com</div>
    </div>

    <div class="front-title">
      <div class="front-title__brand">NOLAN WHITBY</div>
      <div class="front-title__product">100% Pure Argan Oil</div>
    </div>

    <div class="front-name">Nolan Whitby</div>
    <div class="front-type">moisturizing oil</div>
    <div class="front-volume">120mL 4 fl. oz</div>

    <div class="copy copy--ingredients">
      <p><strong>Ingredients:</strong> Lorem ipsum dolor sit amet, consectetur adipiscing elit. Suspendisse eu justo augue. Suspendisse pretium lorem id varius iaculis. Pellentesque vehicula tellus non tincidunt ornare. Curabitur quis turpis diam. Proin vitae euismod ex. Nulla eget luctus massa.</p>
    </div>

    <div class="copy copy--directions">
      <p><strong>Directions:</strong> Apply liberally and massage on to your skin.</p>
    </div>

    <div class="shelf-life">
      <svg width="18" height="16" viewBox="0 0 18 16" aria-hidden="true">
        <g fill="none" stroke="var(--label-ink)" stroke-width="0.9">
          <path d="M2 6 L2 14 Q2 15 3 15 L15 15 Q16 15 16 14 L16 6"/>
          <ellipse cx="9" cy="6" rx="7" ry="2"/>
          <path d="M3 4 L4 1.5 L16 2.5 L16 5"/>
        </g>
      </svg>
      <span>24M</span>
    </div>
  </section>

  <div class="wordmark wordmark--stacked">
    <div class="wordmark__dot"></div>
    <div class="wordmark__text">NOLAN WHITBY</div>
  </div>
  <div class="wordmark wordmark--monogram">Nolan<br>Whitby</div>
  <div class="wordmark wordmark--line">NOLAN WHITBY</div>

  <div class="footer-band"></div>
</body>
</html>
```